Design Brief for Website Redesign

Client Name: Bluecrest IT
Website: www.bluecrestit.com.au
Industry: Managed IT Services
Target Audience: Small to medium-sized businesses in Australia, requiring IT solutions, IT support, cloud services, and phone systems.

Project Overview
We are seeking a full redesign of the Bluecrest IT website to modernize its look, improve usability, and enhance user experience across devices. The goal is to create a professional, clean, and user-friendly website that reflects our expertise in IT services and appeals to our business clients.

Objectives
Modern Visual Identity: Create a fresh, modern design that aligns with Bluecrest IT's branding.

Improved User Experience: Simplify navigation, improve accessibility, and enhance mobile responsiveness.

Clear Calls to Action: Ensure CTAs are prominent and encourage user engagement.

Enhanced Trust & Credibility: Highlight testimonials, case studies, and industry credentials.

SEO Optimization: Ensure the site is optimized for search engines, including proper heading structures and metadata.
Design Style & Tone
Professional: Clean, modern, and polished to reflect our IT expertise.

Minimalist: Simple layouts, plenty of white space, and easy-to-read typography.

Tech-focused: Subtle tech-themed design elements that reinforce our brand as a leading IT service provider.

Colors: Use our existing brand colors, or propose a color scheme that complements the tech industry while maintaining a professional feel.

Typography: Clear, readable fonts that convey professionalism and trustworthiness.

Key Pages & Features
Home Page:

Hero section with a clear value proposition.

Highlight key services (IT support, cloud solutions, phone systems, etc.) with icons and brief descriptions.

Prominent CTAs (e.g., “Request a Quote,” “Book a Demo”).

Testimonials from satisfied clients.

Services Page:

Detailed breakdown of the services we offer (IT support, cloud services, phone systems, etc.).

Use of icons or illustrations to make the services visually engaging.

Clear CTAs to request quotes or book consultations.

About Us Page:

Information about our company history, mission, and team.

Highlight our certifications, partnerships, and industry expertise.

Case Studies/Testimonials Page:

Showcase client success stories and testimonials with visuals and brief case study summaries.

Include a trust-building section with logos of major clients or partners.

Contact Page:

Simple contact form for inquiries.

Integrated map with office location.

Social media links and phone number.

Blog/Resource Section:

Easy-to-navigate blog section for IT-related articles, tips, and industry news.

Clear categorization and tags for easy browsing.

Knowledge Base/Support Page:

Self-service area for clients to find articles, FAQs, and support guides.

Option to submit a support ticket.

Mobile Responsiveness:

Ensure the design is fully responsive, with no horizontal scrolling or misaligned content on mobile.

Functional Requirements
Fast Load Times: Optimize images, minimize unnecessary scripts, and ensure the site loads quickly on both desktop and mobile.

User-Friendly CMS: We need a CMS that is easy to update (preferably WordPress, but open to other suggestions).

SEO Best Practices: Structure the site with proper metadata, alt tags, and semantic HTML for better search engine optimization.

Security: Ensure the website follows security best practices (SSL, HTTPS).

Deliverables
Full website design (desktop and mobile versions).

Design mockups in Photoshop, Sketch, or Figma (whichever is preferred).

Working prototype (optional).

Final website files, including images and assets.

A style guide for ongoing consistency.

Industry/Entity Type

IT Managed Services

Number of Pages Required

3 page

Requirements
Must have
• EXCELLENT UX/UI

```html
<!DOCTYPE html>
<html lang="en">
<head>
<meta charset="utf-8">
<title>Bluecrest IT – Website Modules</title>
<link href="https://fonts.googleapis.com/css2?family=Roboto:wght@400;500;700;900&display=swap" rel="stylesheet">
<style>
:root{
  --ink:#0b0b0b;
  --dark:#110003;
  --dark-2:#1d0206;
  --red:#e0173a;
  --red-deep:#a3142c;
  --wine:#3a0610;
  --white:#ffffff;
  --muted:#d9c5c9;
  --line:#e3e3e3;
}
*{margin:0;padding:0;box-sizing:border-box}
html,body{width:704px;height:1200px;overflow:hidden;background:var(--white);font-family:'Roboto',Arial,sans-serif;color:var(--ink)}
.board-title{position:absolute;left:74px;font-size:24px;font-weight:900;letter-spacing:-.2px;line-height:1}
.panel{position:absolute;left:74px;width:556px;background:var(--dark);overflow:hidden;color:var(--white)}
.wave{position:absolute;left:0;right:0;bottom:0;height:110px;background:radial-gradient(ellipse at 60% 100%,rgba(190,20,45,.75),rgba(120,8,25,.35) 45%,transparent 70%)}
/* hero + nav */
.logo{position:absolute;left:63px;top:19px;font-size:9.5px;font-weight:700;color:var(--white);white-space:nowrap;line-height:1}
.nav{position:absolute;top:22px;font-size:5.5px;color:var(--white);white-space:nowrap;line-height:1}
.nav.active{color:var(--red)}
.btn{position:absolute;display:flex;align-items:center;justify-content:center;border-radius:12px;font-size:5.3px;font-weight:500;white-space:nowrap}
.btn-light{background:var(--white);color:var(--ink)}
.btn-red{background:var(--red);color:var(--white)}
.text-link{position:absolute;font-size:5.3px;font-weight:500;color:var(--white);white-space:nowrap}
.hero-word{position:absolute;left:394px;top:98px;font-size:22px;font-weight:700}
.hero-line{position:absolute;left:387px;top:169px;font-size:9px}
.mega{position:absolute;left:64px;top:36px;width:324px;height:170px;background:var(--white);color:var(--ink)}
.mega-card{position:absolute;width:96px;height:46px;border:1px solid var(--line);padding:5px 6px}
.mega-card h4{font-size:5.4px;font-weight:500;display:flex;align-items:center;gap:3px;white-space:nowrap}
.mega-card p{font-size:4.2px;line-height:7px;color:#333;margin-top:2px}
.mega-card a{display:block;font-size:4.2px;font-weight:500;color:var(--ink);text-decoration:none;margin-top:2px;white-space:nowrap}
.icon{width:9px;height:9px;flex:none}
/* services */
.section-heading{position:absolute;left:0;right:0;text-align:center;font-size:14px;font-weight:500}
.section-intro{position:absolute;left:100px;right:100px;text-align:center;font-size:4.3px;line-height:7px;color:var(--muted)}
.svc-card{position:absolute;width:134px;height:106px;border-radius:4px;background:linear-gradient(180deg,#1e0307,#2c050c);padding:15px 13px}
.svc-card.featured{background:linear-gradient(180deg,#b0132d,#8a0f22)}
.svc-card .svc-icon{width:15px;height:15px}
.svc-card h3{position:absolute;left:13px;top:52px;font-size:8.3px;font-weight:500;white-space:nowrap}
.svc-card p{position:absolute;left:13px;right:10px;top:67px;font-size:4.3px;line-height:7px;color:var(--muted)}
.svc-card a{position:absolute;left:13px;top:85px;font-size:4.6px;font-weight:500;color:var(--white);text-decoration:none;white-space:nowrap}
/* case study */
.eyebrow{position:absolute;left:65px;top:16px;font-size:7px;color:var(--red);font-weight:500}
.case-headline{position:absolute;left:65px;top:28px;font-size:14.5px;font-weight:500;white-space:nowrap}
.device-shot{position:absolute;left:67px;top:72px;width:164px;height:137px;border-radius:5px;background:linear-gradient(160deg,#1b2140,#0d1020 60%,#2a2d35)}
.client-name{position:absolute;left:252px;top:73px;font-size:8.5px;font-weight:500}
.client-copy{position:absolute;left:252px;width:232px;font-size:4.3px;line-height:7px;color:var(--muted)}
.stats-box{position:absolute;left:191px;top:135px;width:297px;height:111px;border-radius:5px;background:linear-gradient(180deg,#4a0711,#6e0c1c);overflow:hidden}
.stat{position:absolute;top:14px}
.stat .num{font-size:11px;font-weight:700;display:flex;align-items:center;gap:3px}
.stat .label{font-size:6.3px;font-weight:500;margin-top:1px;white-space:nowrap}
.words{position:absolute;left:11.5px;top:50px;font-size:6px;font-weight:500}
.quote-copy{position:absolute;left:11.5px;right:10px;top:62px;font-size:4.2px;line-height:7px;color:var(--muted)}
.quote-mark{position:absolute;right:10px;top:44px;font-size:42px;font-weight:900;color:rgba(255,255,255,.15);line-height:1}
</style>
</head>
<body>

<h1 class="board-title" style="top:74px">Mega Menu Design</h1>
<section class="panel" style="top:113px;height:246px">
  <div class="wave" role="img" aria-label="Red particle wave background"></div>
  <div class="logo">Bluecrest IT</div>
  <span class="nav active" style="left:130px">Services &#8963;</span>
  <span class="nav" style="left:176px">Solutions &#8964;</span>
  <span class="nav" style="left:223px">About Us</span>
  <span class="nav" style="left:263px">Resources &#8964;</span>
  <span class="nav" style="left:314px">Shop</span>
  <span class="nav" style="left:344px">Contact Us</span>
  <div class="btn btn-light" style="left:427px;top:18px;width:59px;height:16px">Book a Demo</div>
  <div class="hero-word">with</div>
  <div class="hero-line">More.</div>

  <div class="mega">
    <div class="mega-card" style="left:11.5px;top:10.5px"><h4><svg class="icon" viewBox="0 0 10 10"><rect x="1" y="2" width="7" height="6" rx="1" fill="#e0173a"/><circle cx="8" cy="2" r="1.5" fill="#e0173a"/></svg>IT Support</h4><p>Lorem ipsum dolor sit amet, consetet sadipscing elitr lorem ipsum.</p><a>Learn More About IT Support &#10230;</a></div>
    <div class="mega-card" style="left:114px;top:10.5px"><h4><svg class="icon" viewBox="0 0 10 10"><rect x="1" y="1" width="8" height="6" rx="1" fill="#e0173a"/><rect x="3" y="8" width="4" height="1" fill="#e0173a"/></svg>IT Project Services</h4><p>Lorem ipsum dolor sit amet, consetet sadipscing elitr lorem ipsum.</p><a>More About IT Project Services &#10230;</a></div>
    <div class="mega-card" style="left:216px;top:10.5px"><h4><svg class="icon" viewBox="0 0 10 10"><rect x="1" y="2" width="8" height="6" rx="1" fill="#e0173a"/><circle cx="5" cy="5" r="1.5" fill="#fff"/></svg>IT Consulting &amp; Training</h4><p>Lorem ipsum dolor sit amet, consetet sadipscing elitr lorem ipsum.</p><a>Learn More About IT Consulting &#10230;</a></div>
    <div class="mega-card" style="left:11.5px;top:62px"><h4><svg class="icon" viewBox="0 0 10 10"><path d="M5 1 9 3 5 5 1 3Z M1 5 5 7 9 5 M1 7 5 9 9 7" fill="none" stroke="#e0173a" stroke-width="1.2"/></svg>Hardware &amp; Software</h4><p>Lorem ipsum dolor sit amet, consetet sadipscing elitr lorem ipsum.</p><a>More About Software Services &#10230;</a></div>
    <div class="mega-card" style="left:114px;top:62px"><h4><svg class="icon" viewBox="0 0 10 10"><rect x="1" y="1" width="8" height="6" rx="1" fill="none" stroke="#e0173a"/><path d="M5 3 7 4V6L5 7 3 6V4Z" fill="#e0173a"/></svg>Cyber Security</h4><p>Lorem ipsum dolor sit amet, consetet sadipscing elitr lorem ipsum.</p><a>Learn More About Cyber Security &#10230;</a></div>
    <div class="mega-card" style="left:216px;top:62px"><h4><svg class="icon" viewBox="0 0 10 10"><ellipse cx="5" cy="4" rx="4" ry="2.5" fill="#e0173a"/><path d="M3 7V9M5 7V9M7 7V9" stroke="#e0173a"/></svg>Cloud Services</h4><p>Lorem ipsum dolor sit amet, consetet sadipscing elitr lorem ipsum.</p><a>Learn More About Cloud Services &#10230;</a></div>
    <div class="mega-card" style="left:11.5px;top:114px"><h4><svg class="icon" viewBox="0 0 10 10"><rect x="1" y="1" width="7" height="8" rx="1" fill="#e0173a"/><circle cx="5" cy="5" r="1.8" fill="#fff"/></svg>IT Auditing</h4><p>Lorem ipsum dolor sit amet, consetet sadipscing elitr lorem ipsum.</p><a>Learn More About IT Auditing &#10230;</a></div>
    <div class="mega-card" style="left:114px;top:114px"><h4><svg class="icon" viewBox="0 0 10 10"><rect x="1" y="2" width="8" height="6" rx="1" fill="#e0173a"/><path d="M4 4 3 5 4 6M6 4 7 5 6 6" stroke="#fff" fill="none" stroke-width=".8"/></svg>Mobile &amp; Web Development</h4><p>Lorem ipsum dolor sit amet, consetet sadipscing elitr lorem ipsum.</p><a>About Mobile &amp; Web Development &#10230;</a></div>
  </div>

  <div class="btn btn-light" style="left:207px;top:208px;width:73px;height:19px">Request a Quote</div>
  <span class="text-link" style="left:286px;top:214px">Explore Services &#10230;</span>
</section>

<h1 class="board-title" style="top:436px">Our Services Module</h1>
<section class="panel" style="top:474px;height:248px">
  <h2 class="section-heading" style="top:16px">Our Services</h2>
  <p class="section-intro" style="top:41px">Lorem ipsum dolor sit amet, consetetur sadipscing elitr, sed diam nonumy eirmod tempor invidunt ut labore et dolore magna. sed diam nonumy eirmod tempor invidunt ut labore et dolore magna.</p>

  <article class="svc-card" style="left:61px;top:73px">
    <svg class="svc-icon" viewBox="0 0 16 16"><rect x="2" y="3" width="12" height="9" rx="1" fill="#fff"/><circle cx="8" cy="7.5" r="2" fill="#2c050c"/></svg>
    <h3>IT Consulting &amp; Training</h3>
    <p>Lorem ipsum dolor sit amet, consetetur sadipscing elitr lorem ipsum.</p>
    <a>Learn More About IT Consulting &#10230;</a>
  </article>
  <article class="svc-card featured" style="left:207px;top:70px">
    <svg class="svc-icon" viewBox="0 0 16 16"><ellipse cx="8" cy="6" rx="6" ry="4" fill="#fff"/><path d="M5 10V14M8 10V14M11 10V14" stroke="#fff"/></svg>
    <h3 style="top:49px">Cloud Services</h3>
    <p style="top:64px">Lorem ipsum dolor sit amet, consetetur sadipscing elitr lorem ipsum.</p>
    <a style="top:82px">Learn More About Cloud Services &#10230;</a>
  </article>
  <article class="svc-card" style="left:352px;top:73px">
    <svg class="svc-icon" viewBox="0 0 16 16"><rect x="2" y="4" width="12" height="8" rx="1" fill="none" stroke="#fff" stroke-width="1.3"/><path d="M6 6 4.5 8 6 10M10 6 11.5 8 10 10" stroke="#fff" fill="none"/><rect x="1" y="13" width="14" height="1.3" fill="#fff"/></svg>
    <h3>Mobile &amp; Web Development</h3>
    <p>Lorem ipsum dolor sit amet, consetetur sadipscing elitr lorem ipsum.</p>
    <a>More About Mobile &amp; Web Development &#10230;</a>
  </article>

  <div class="btn btn-red" style="left:198px;top:203px;width:86px;height:19px">View all our Services</div>
  <span class="text-link" style="left:293px;top:209px">Request a Quote &#10230;</span>
</section>

<h1 class="board-title" style="top:795px">Case Studies Module</h1>
<section class="panel" style="top:836px;height:274px;width:558px">
  <div class="eyebrow">Case Studies</div>
  <h2 class="case-headline">Lorem ipsum dolor sit amet, consetetur sadipscing dolor</h2>
  <div class="device-shot" role="img" aria-label="Tablet showing the redesigned client homepage"></div>
  <h3 class="client-name">Client’s Name Goes Here</h3>
  <p class="client-copy" style="top:92px">Lorem ipsum dolor sit amet, consetetur sadipscing elitr, sed diam nonumy eirmod tempor invidunt ut labore et dolore magna aliquyam erat.</p>
  <p class="client-copy" style="top:113px">Sed diam voluptua. At vero eos et accusam et justo duo dolores et ea rebum. Stet clita kasd gubergren, no sea takimata sanctus est Lorem ipsum dolor sit amet.</p>

  <div class="stats-box">
    <div class="stat" style="left:11.5px"><div class="num"><svg width="10" height="10" viewBox="0 0 10 10"><circle cx="3" cy="3" r="1.6" fill="#fff"/><circle cx="7" cy="3" r="1.6" fill="#fff"/><rect x="1" y="5.5" width="8" height="3.5" rx="1" fill="#fff"/></svg>000+</div><div class="label">Loren Ipsum</div></div>
    <div class="stat" style="left:84px"><div class="num"><svg width="10" height="10" viewBox="0 0 10 10"><path d="M1 4 5 1 9 4Z" fill="#fff"/><rect x="2" y="4.5" width="1.3" height="3.5" fill="#fff"/><rect x="4.4" y="4.5" width="1.3" height="3.5" fill="#fff"/><rect x="6.8" y="4.5" width="1.3" height="3.5" fill="#fff"/><rect x="1" y="8.5" width="8" height="1" fill="#fff"/></svg>000%</div><div class="label">Loren Ipsum</div></div>
    <div class="stat" style="left:157px"><div class="num"><svg width="8" height="11" viewBox="0 0 8 11"><rect x="1" y="0.5" width="6" height="10" fill="none" stroke="#fff"/><rect x="1" y="0.5" width="3" height="10" fill="#fff"/></svg>00k</div><div class="label">Loren Ipsum</div></div>
    <div class="stat" style="left:228px"><div class="num"><svg width="8" height="11" viewBox="0 0 8 11"><path d="M4 10.5C1 6.5 0.5 5 0.5 4A3.5 3.5 0 0 1 7.5 4C7.5 5 7 6.5 4 10.5Z" fill="#fff"/><circle cx="4" cy="4" r="1.3" fill="#6e0c1c"/></svg>Texas</div><div class="label">Loren Ipsum dolor</div></div>
    <div class="quote-mark">&#8221;</div>
    <div class="words">Words from the Client</div>
    <p class="quote-copy">Lorem ipsum dolor sit amet, consetetur sadipscing elitr, sed diam nonumy eirmod tempor invidunt ut labore et dolore magna aliquyam erat. Sed diam voluptua. At vero eos et accusam et justo duo dolores et ea rebum. Stet clita kasd gubergren, no sea takimata sanctus est Lorem ipsum dolor sit amet. Lorem ipsum dolor sit amet, consetetur sadipscing elitr, sed diam nonumy eirmod tempor invidunt ut labore et dolore magna aliquyam erat. Sed diam voluptua. At vero eos et accusam et justo duo dolores et ea rebum. Stet clita kasd gubergren.</p>
  </div>

  <div class="btn btn-red" style="left:65px;top:226px;width:86px;height:19px">View all Case Studies</div>
</section>

</body>
</html>
```